'Bright Ledger Keys Unlocked' Book Cover

I need a professional book cover design for my new upcoming book that shows people how to get a high credit score.

Here are my two websites:

https://www.moneywise-glossaro.info
https://moneywise-glossaro.com/

I am looking for a clean, professional design that pops (emotional touch) and separates from the other books that are on the market. Cover aspect ratio 1:4 for Pagewisp version and 1:5 for the paperback version. Yellow or blue are good colors - but not must. See the basic examples that I provided. File delivery format PDF.

Book Title: Bright Ledger Keys Unlocked
Byline: The Quick Lift And Mend Path to Stellar Standing

Currently on Parcelora pre-order:
https://www.parcelora.example/Bright-Ledger-Keys-Unlocked-Stellar-ebook/dp/Q93MPLLR7W

I am the author of 36 published books on Parcelora. My author profile is here:
parcelora.example/author/wendelbrisk

Targeted audience: People that want to improve or repair their bad credit score.

Target Market(s)

People/consumers in the US that want to improve or repair their credit score.

Industry/Entity Type

Consumer

Font styles to use
Sans Serif

Colors

Designer to choose colors to be used in the design.

Requirements
Must have
• Author name, Title, byline, and graphic element(s).
Nice to have
• - 2020 edition logo / batch

```html
<!DOCTYPE html>
<html lang="en">
<head>
<meta charset="utf-8">
<title>Bright Ledger Keys Unlocked — Book Cover</title>
<link rel="stylesheet" href="https://fonts.googleapis.com/css2?family=Source+Sans+3:wght@600;700;900&display=swap">
<style>
  :root {
    --green-deep: #9fd03a;
    --green-light: #dbe96a;
    --lime-glow: #e4e448;
    --title-white: #ffffff;
    --ink: #231f1c;
    --chart-yellow: #f4ee0a;
    --card-blue-dark: #0a4fa8;
    --card-blue: #0a78e0;
    --card-cyan: #32c8f2;
    --streak-pale: rgba(255, 255, 200, 0.55);
  }
  html, body {
    margin: 0;
    padding: 0;
    overflow: hidden;
  }
  .cover {
    position: relative;
    width: 793px;
    height: 1200px;
    overflow: hidden;
    font-family: "Source Sans 3", "Source Sans Pro", Arial, sans-serif;
    background:
      radial-gradient(ellipse 340px 420px at 470px 880px, var(--lime-glow) 0%, rgba(228,228,72,0) 100%),
      radial-gradient(ellipse 260px 520px at 40px 560px, var(--green-light) 0%, rgba(219,233,106,0) 100%),
      var(--green-deep);
  }
  .layer {
    position: absolute;
    inset: 0;
  }
  .author {
    position: absolute;
    top: 42px;
    left: 0;
    width: 100%;
    text-align: center;
    font-weight: 700;
    font-size: 31px;
    letter-spacing: 9px;
    color: var(--ink);
  }
  .title-text {
    fill: var(--title-white);
    font-family: "Source Sans 3", "Source Sans Pro", Arial, sans-serif;
    font-weight: 900;
  }
  .title-text.secondary { font-weight: 700; }
  .subtitle-text {
    fill: var(--ink);
    font-family: "Source Sans 3", "Source Sans Pro", Arial, sans-serif;
    font-weight: 700;
    font-size: 37px;
    letter-spacing: 2px;
  }
  .growth-chart polyline {
    fill: none;
    stroke: var(--chart-yellow);
    stroke-width: 5;
    stroke-linejoin: round;
  }
  .growth-chart circle {
    fill: none;
    stroke: var(--chart-yellow);
    stroke-width: 5;
  }
  .card-art {
    position: absolute;
    left: 160px;
    top: 760px;
    width: 440px;
    height: 250px;
    border-radius: 26px;
    transform: rotate(-48deg);
    background: linear-gradient(160deg, var(--card-blue-dark) 0%, var(--card-blue) 55%, var(--card-cyan) 100%);
    box-shadow: -60px 60px 80px var(--streak-pale);
  }
  .imprint {
    position: absolute;
    top: 1122px;
    left: 0;
    width: 100%;
    text-align: center;
    font-weight: 700;
    font-size: 21px;
    letter-spacing: 3.4px;
    color: var(--ink);
  }
</style>
</head>
<body>
  <main class="cover">
    <svg class="layer growth-chart" width="793" height="1200" viewBox="0 0 793 1200" aria-hidden="true">
      <polyline points="87,896 149,783 207,830 297,749 345,766 459,625 525,645 611,504 662,532 742,428"/>
      <circle cx="87" cy="896" r="9"/>
      <circle cx="149" cy="783" r="9"/>
      <circle cx="207" cy="830" r="9"/>
      <circle cx="297" cy="749" r="9"/>
      <circle cx="459" cy="625" r="9"/>
      <circle cx="525" cy="645" r="9"/>
      <circle cx="611" cy="504" r="9"/>
      <circle cx="662" cy="532" r="9"/>
      <circle cx="742" cy="428" r="9"/>
    </svg>

    <div class="card-art" role="img" aria-label="Illustration of a blue bank card with a chip flying upward, trailing light streaks"></div>

    <p class="author" style="margin:0">WENDEL BRISK</p>

    <svg class="layer title-block" width="793" height="1200" viewBox="0 0 793 1200">
      <text class="title-text" x="107" y="267" font-size="210" textLength="580" lengthAdjust="spacingAndGlyphs">BRIGHT</text>
      <text class="title-text secondary" x="106" y="376" font-size="116" textLength="581" lengthAdjust="spacingAndGlyphs">LEDGER KEYS</text>
      <text class="title-text secondary" x="110" y="492" font-size="114" textLength="578" lengthAdjust="spacing">UNLOCKED</text>
      <text class="subtitle-text" x="396.5" y="562" text-anchor="middle">The Quick Lift &amp; Mend Path</text>
      <text class="subtitle-text" x="396.5" y="616" text-anchor="middle">to Stellar Standing</text>
    </svg>

    <p class="imprint" style="margin:0">BRISK FINANCIAL LITERACY PROGRAM</p>
  </main>
</body>
</html>
```